Box for baby swaddle blankets.

Hi there!

I'd like you to make a packaging design for the box of my muslin swaddle blankets which I'll be selling on Pindlewick.com. I want the product to be the perfect baby shower gift! Most of the packages of my competitors are made by the manufacturing company, so they're pretty simple and similar to each other, I'd like you to make a unique design for me. I included a detailed description about the parameters in the "must haves" section. If you have any questions or suggestions, please message me.

Target Market(s)

Pindlewick.com

Industry/Entity Type

Baby Care

Colors

Designer to choose colors to be used in the design.

Requirements
Must have
• 1. Most of my competitors use pretty basic packaging, so I'd like stand out with my box. I was thinking about putting my logo at the bottom of the front side, and make heart-shaped cuts above the elephant's trunk, which would allow buyers to see the fabric and the pattern of the blankets. You can remove the heart from my logo since I think it wouldn't look good with the cuts above it. Tell me what you think about this, I'm also open for other ideas for the front as well as long as it makes the packaging unique and gives the buyers a peek of the blankets.
• I attached some examples of cuts I've seen on packages.
• 2. I'd like you to use the title BABY SWADDLE BLANKETS and my logo on the front. The package contains 3 blankets are made from organic muslin cotton with 47x47 inch size, you could include this also in the front if you can find a good way for it .
• Also, I'd like to have a stamp of 100% ORGANIC COTTON in one corner.
• The package will contain a bonus baby bandana bib, so please put a BANDANA BIB GIFT INSIDE! object with an arrow pointing in the box in the front.
• 3. For the sides, one of them should show the different ways you can use these blankets, with illustrations. I'll attach some examples for this (I like the pictogram-type illustration on img1 better) . You can add my logo for the top side. You can try to add the words "BREATHABLE" "EXTRA SOFT" "LARGE SIZE" "100% ORGANIC COTTON" on the remaining side(s) if it would look good in your opinion.
• 4. For the back, I'd like you to add a 4-step instruction about how to swaddle the baby with the blankets. Since almost all of competitors use the same images, I'd like you to design new ones, make it playful and baby-friendly :) I'll attach some examples for these instructions as well.. The bottom of the back should contain the text "Made with care in China, designed with love in the United States" and a place for the barcode.
• 4. The box should be the size of 21*22*8 in centimeters.
• If you have any questions or suggestions for the design, please message me.
Nice to have
• If you have any other ideas or suggestions about the design, feel free to contact me.

```html
<!DOCTYPE html>
<html lang="en">
<head>
<meta charset="utf-8">
<title>Baby Swaddle Blankets – Box Front</title>
<link href="https://fonts.googleapis.com/css2?family=Gochi+Hand&display=swap" rel="stylesheet">
<style>
  :root {
    --page-bg: #f4f2ee;
    --kraft: #c2ab83;
    --kraft-band: #bda57c;
    --cocoa: #54453c;
    --ink-white: #ffffff;
    --gift-yellow: #f2b62a;
    --fabric-light: #f7fafb;
    --fabric-blue: #bcdbe8;
    --fabric-teal: #5fb9ad;
    --brand-blue: #6fa9d6;
  }
  html, body {
    margin: 0;
    padding: 0;
    width: 1200px;
    height: 1000px;
    overflow: hidden;
    background: var(--page-bg);
  }
  .canvas {
    position: relative;
    width: 1200px;
    height: 1000px;
  }
  .box-front {
    position: absolute;
    left: 270px;
    top: 130px;
    width: 660px;
    height: 740px;
    box-shadow: 0 20px 40px rgba(0,0,0,0.12);
  }
  .box-front svg { display: block; overflow: hidden; }
  .hand {
    font-family: "Gochi Hand", cursive;
  }
  .title-big { font-size: 84px; fill: var(--ink-white); }
  .title-small { font-size: 50px; fill: var(--ink-white); }
  .stamp-text { font-size: 19px; fill: var(--ink-white); letter-spacing: 2px; }
  .gift-text { font-size: 26px; fill: var(--gift-yellow); letter-spacing: 1px; }
  .pack-text { font-size: 25px; fill: var(--ink-white); letter-spacing: 1px; }
  .brand-name { font-size: 38px; fill: var(--brand-blue); }
</style>
</head>
<body>
<div class="canvas">
  <div class="box-front">
    <svg width="660" height="740" viewBox="0 0 660 740" xmlns="http://www.w3.org/2000/svg">
      <defs>
        <linearGradient id="fabricTones" x1="0" y1="0" x2="1" y2="0">
          <stop offset="0" stop-color="var(--fabric-teal)" stop-opacity="0.55"/>
          <stop offset="0.35" stop-color="var(--fabric-light)"/>
          <stop offset="0.55" stop-color="var(--fabric-blue)"/>
          <stop offset="0.8" stop-color="var(--fabric-light)"/>
          <stop offset="1" stop-color="var(--fabric-teal)" stop-opacity="0.6"/>
        </linearGradient>
      </defs>

      <rect class="face" width="660" height="740" fill="var(--kraft)"/>

      <path class="gift-panel" d="M0 300 L330 650 L0 650 Z" fill="var(--cocoa)"/>

      <path class="heart-window" role="img" aria-label="Heart-shaped window showing three folded muslin blankets with triangle, sun-and-wave and whale patterns in teal, light blue and beige"
            d="M330 120 C300 40,200 20,120 40 C40 60,10 140,20 230 C35 380,200 520,330 650 C460 520,625 380,640 230 C650 140,620 60,540 40 C460 20,360 40,330 120 Z"
            fill="url(#fabricTones)"/>

      <text class="hand stamp-text" x="355" y="28" transform="rotate(10 355 28)">100% ORGANIC COTTON</text>

      <path class="title-band" d="M0 150 L660 118 L660 262 L0 292 Z" fill="var(--kraft-band)"/>
      <g transform="rotate(-3 330 210)">
        <text class="hand title-big" x="30" y="262">Baby</text>
        <text class="hand title-small" x="215" y="236">Swaddle Blankets</text>
      </g>

      <g transform="rotate(-9 20 500)">
        <text class="hand gift-text" x="20" y="500">BANDANA BIB</text>
        <text class="hand gift-text" x="30" y="532">GIFT INSIDE!</text>
      </g>
      <path class="gift-arrow" d="M95 585 Q170 610 235 560" fill="none" stroke="var(--gift-yellow)" stroke-width="3" stroke-linecap="round"/>
      <path d="M218 558 L236 559 L231 576" fill="none" stroke="var(--gift-yellow)" stroke-width="3" stroke-linecap="round" stroke-linejoin="round"/>

      <circle class="brand-dot" cx="392" cy="608" r="9" fill="var(--brand-blue)"/>
      <text class="hand brand-name" x="410" y="622">Snugglora</text>

      <text class="hand pack-text" x="14" y="705">3 Pack Muslin Blanket</text>
    </svg>
  </div>
</div>
</body>
</html>
```